Label / Packaging design for supplements bottle (capsule bottle)

We are a startup supplements company focusing on animal nutrition. The task here is to design the supplement bottles for the product series. Think of bodybuilding supplement packaging more than health&wellness type of packaging.

The brandname is Roost Vector

The goal is to have 3 bottles with similar/identical designs but with different color accents (i.e. red for one bottle, yellow for the second, (not green or blue) for the third).

The bottles can either be black theme or white theme. I'll leave it up to the designer.

Final design should communicate bodybuilding (bold fonts preferred)

Logo files below (both SVG and AI files), the insignia can be used independently of the text and slogan, or it can be positioned above brand name or beside it.
*Feel free to change the color of the insignia and text to match your chosen accent color for the bottle!*

Bottle size will be approximately 11.9cm x 6.35cm (Height x circumference) (height is from bottom to mouth opening)
Thus, label size at the moment can be designed 6.30cm x 10cm (L x W)

Target Market(s)

Male, Adult

Industry/Entity Type

It Company

Font styles to use
Sans Serif

Requirements
Must have
• Text: "Performance Enhancing Supplements for Racing Pigeons"
• Essentials
• "240 Capsules"
• Bottle 1:
• Creatine+Carnitine
• Text + Imagery:*see Carnitine Benefits.png
• Bottle 2:
• BCAA
• Text:
• SUPPORT MUSCLE PROTEIN SYNTHESIS
• DECREASE PROTEIN CATABOLISM
• PROMOTE INSULIN SENSITIVITY
• Offset Muscle Breakdown and Increase Muscular Endurance
• ENHANCED RECOVERY FROM EXERCISE
• Promotes Lowered Body Fat Levels, Increased Strength, & Improves Muscle Repair
• (Imagery can use the same as bottle 1 similar to Carnitine Benefits.png)
• Bottle 3:
• Vitamins
• Text: Supports Rigorous Training and Needs To Support Growth and Overall Well-being
• Spaces for Text for:
• 1.) Directions for Use
• 2.) Developed by:
• 3.) Ingredients
Nice to have
• Mosaic/Pattern subtle fading background (e.g. honeycomb etc)
• Prominent "A" "B" "C" on each bottle,
• A for Armor Vitamins
• B for BCAA
• C for Carnitine/Creatine Complex
• ABC Essential Series

```html
<!DOCTYPE html>
<html lang="en">
<head>
<meta charset="utf-8">
<title>Roost Vector – Supplement Labels</title>
<link rel="stylesheet" href="https://fonts.googleapis.com/css2?family=Montserrat:wght@300;400;700;900&family=Exo+2:ital,wght@1,900&display=swap">
<style>
  :root {
    --page-bg: #ffffff;
    --label-grey: #6f6f6f;
    --label-grey-dark: #3a3a3a;
    --accent-red: #5a1216;
    --accent-red-dark: #3d0b0e;
    --bright-red: #d8141c;
    --text-white: #ffffff;
    --text-soft: #e6e6e6;
  }
  * { box-sizing: border-box; margin: 0; padding: 0; }
  html, body { width: 1200px; height: 1200px; overflow: hidden; background: var(--page-bg); }
  .canvas { position: relative; width: 1200px; height: 1200px; }

  .label {
    position: absolute; top: 340px; width: 560px; height: 520px;
    overflow: hidden; font-family: "Montserrat", sans-serif; color: var(--text-white);
  }
  .label--classic { left: 25px; }
  .label--italic { left: 615px; }

  .label__photo {
    position: absolute; left: 0; top: 0; width: 47%; height: 100%;
    background: radial-gradient(ellipse at 55% 45%, #1d1d1d 0%, #4a4a4a 45%, var(--label-grey) 80%);
  }
  .label__accent {
    position: absolute; left: 47%; top: 0; width: 53%; height: 100%;
    background: linear-gradient(180deg, var(--accent-red) 0%, var(--accent-red-dark) 100%);
  }

  .brand-mark {
    position: absolute; top: 50px; left: 0; width: 100%; text-align: center;
    font-weight: 700; font-size: 20px; letter-spacing: 3px; text-transform: uppercase;
  }
  .brand-mark__dot {
    display: inline-block; width: 14px; height: 14px; border-radius: 50%;
    background: var(--text-white); margin-right: 10px; vertical-align: middle; position: relative; top: -2px;
  }

  .series-badge {
    position: absolute; top: 92px; left: 378px; display: flex; align-items: center; gap: 8px;
    font-size: 12px; font-weight: 400; line-height: 1.2; text-transform: uppercase;
  }
  .series-badge__letter {
    width: 44px; height: 44px; border-radius: 50%; border: 1.5px solid var(--bright-red);
    color: var(--bright-red); display: flex; align-items: center; justify-content: center;
    font-size: 18px; font-weight: 300;
  }

  .product-title {
    position: absolute; left: 0; width: 100%; text-align: center; text-transform: uppercase;
  }
  .label--classic .product-title {
    top: 150px; font-weight: 900; font-size: 86px; line-height: 0.95; letter-spacing: -1px;
  }
  .label--italic .product-title {
    top: 205px; font-family: "Exo 2", sans-serif; font-style: italic; font-weight: 900;
    font-size: 54px; letter-spacing: -1px; white-space: nowrap;
  }

  .tagline {
    position: absolute; top: 272px; left: 60px; width: 440px; display: flex; align-items: center; gap: 12px;
    font-weight: 700; font-size: 17px; letter-spacing: 3px; color: #8a8a8a; text-transform: uppercase;
  }
  .tagline::before, .tagline::after { content: ""; flex: 1; height: 2px; background: var(--text-soft); }

  .claim {
    position: absolute; left: 0; width: 100%; text-align: center; text-transform: uppercase;
    font-weight: 300; font-size: 24px; line-height: 1.35; letter-spacing: 1px; color: var(--text-soft);
  }
  .label--classic .claim { top: 330px; }
  .label--italic .claim { top: 320px; }
  .claim__target { display: block; color: var(--bright-red); font-size: 28px; margin-top: 2px; }

  .capsule-stamp { position: absolute; left: 446px; top: 368px; width: 104px; height: 104px; }
</style>
</head>
<body>
<main class="canvas">

  <section class="label label--classic">
    <div class="label__photo" role="img" aria-label="Black and white close-up photograph of a spread pigeon wing"></div>
    <div class="label__accent"></div>
    <div class="brand-mark"><span class="brand-mark__dot"></span>Roost Vector</div>
    <div class="series-badge">
      <span class="series-badge__letter">C</span>
      <span>Carnitine/<br>Creatine Complex</span>
    </div>
    <h1 class="product-title">Roost<br>Vector</h1>
    <p class="claim">Performance Enhancing<br>Supplements for<span class="claim__target">Racing Pigeons</span></p>
    <svg class="capsule-stamp" viewBox="0 0 104 104" aria-label="240 capsules">
      <defs><path id="ringA" d="M52,52 m-38,0 a38,38 0 1,1 76,0 a38,38 0 1,1 -76,0"/></defs>
      <circle cx="52" cy="52" r="50" fill="none" stroke="#e6e6e6" stroke-width="1.2"/>
      <circle cx="52" cy="52" r="26" fill="none" stroke="#e6e6e6" stroke-width="1"/>
      <text font-family="Montserrat, sans-serif" font-size="9" fill="#e6e6e6" letter-spacing="1"><textPath href="#ringA">CAPSULES · CAPSULES · CAPSULES · CAPSULES ·</textPath></text>
      <text x="52" y="60" text-anchor="middle" font-family="Montserrat, sans-serif" font-size="22" fill="#e6e6e6" transform="rotate(12 52 52)">240</text>
    </svg>
  </section>

  <section class="label label--italic">
    <div class="label__photo" role="img" aria-label="Black and white close-up photograph of a spread pigeon wing"></div>
    <div class="label__accent"></div>
    <div class="brand-mark"><span class="brand-mark__dot"></span>Roost Vector</div>
    <div class="series-badge">
      <span class="series-badge__letter">C</span>
      <span>Carnitine/<br>Creatine Complex</span>
    </div>
    <h1 class="product-title">Roost Vector</h1>
    <p class="tagline">The Secret of Success</p>
    <p class="claim">Performance Enhancing<br>Supplements for<span class="claim__target">Racing Pigeons</span></p>
    <svg class="capsule-stamp" viewBox="0 0 104 104" aria-label="240 capsules">
      <defs><path id="ringB" d="M52,52 m-38,0 a38,38 0 1,1 76,0 a38,38 0 1,1 -76,0"/></defs>
      <circle cx="52" cy="52" r="50" fill="none" stroke="#e6e6e6" stroke-width="1.2"/>
      <circle cx="52" cy="52" r="26" fill="none" stroke="#e6e6e6" stroke-width="1"/>
      <text font-family="Montserrat, sans-serif" font-size="9" fill="#e6e6e6" letter-spacing="1"><textPath href="#ringB">CAPSULES · CAPSULES · CAPSULES · CAPSULES ·</textPath></text>
      <text x="52" y="60" text-anchor="middle" font-family="Montserrat, sans-serif" font-size="22" fill="#e6e6e6" transform="rotate(12 52 52)">240</text>
    </svg>
  </section>

</main>
</body>
</html>
```